E-Commerce Marketing Banners For Memory- and SSD Company

To design captivating marketing banners for Vextra/Qilo/etc. for an e-commerce company specializing in computer memory and SSDs.
The design should be sleek, modern, and tech-savvy to reflect the company's focus on cutting-edge technology products.
Scope of work
- Creation of multiple marketing banners in 1600x1600 Pixels
- Total of 4 Marketing/Teaser Images for Vextra/Qilo/etc.
- All Images need to Include the Text in German (Large) and English (Below German, 50% Smaller)
Image 1: Performance & Stability & Compatibility
- Use Words Like:
-- Downwards Compatible 1600 -> 1333 -> 1066 Mhz (for DDR3)
-- QUORV Compliance / QUORV Standard
Image 2: Quality & Major Brand Chips
ATTENTION: The Immage MUST NOT have Brand Names like Torvell, Pelka or Dravis. Just the Chips should be displayed very large
- Use Words Like:
-- Only Original Major Brand Chips
-- High Quality Manufacturing
-- High Quality Materials
-- Gold Plated Contacts
Image 3: Lifetime Warranty
- Use Words Like
-- Lifetime Warranty
-- No Questions Asked
-- Cost Free Replacement in 2 Business Days
Image 4: Innovative packaging
- This is our own packaging made of Paper (see Images)
- Use Words Like
-- 95% Less Plastic
-- Good for the Planet
-- Innovative Packaging
Banners must be optimized for web usage, with high-resolution options available for larger displays.
- Banners have to be delivered as 1600x1600 JPEG Format
- Source Files (PSD/AI/etc) + Used Fonts have to be included
Additional information
! All Images have to be Created for SO-DIMM (Laptop), DIMM (Desktop) and SSDs.
Designs can be the same for the different Formats (SO-DIMM, DIMM, SSDs), but text/modules might slightly vary.
- We can provide .step Files for Modules if needed
- We will provide better Pictures of the Package
- There will be a follow up Project on this as well
Updates
Low design quality
Target Market(s)
Ecommerce

```html
<!DOCTYPE html>
<html lang="de">
<head>
<meta charset="utf-8">
<title>Kernova Marketing Banners</title>
<link rel="stylesheet" href="https://fonts.googleapis.com/css2?family=Lato:wght@300;400;700;900&family=Poppins:wght@600;700&family=Roboto:wght@400;500&display=swap">
<style>
  :root {
    --page-bg: #e5e4e7;
    --deep-blue: #3b86c1;
    --sky-blue: #4ba6d9;
    --band-blue: #4c9fd0;
    --pale-grey: #e5eaef;
    --charcoal: #333136;
    --ink: #2e2d32;
    --white: #ffffff;
  }
  * { margin: 0; padding: 0; box-sizing: border-box; }
  html, body { width: 1200px; height: 4286px; overflow: hidden; }
  body { background: var(--page-bg); position: relative; }

  .banner {
    position: absolute; left: 143px; width: 914px; height: 914px;
    overflow: hidden; box-shadow: 0 6px 18px rgba(0,0,0,0.18);
  }
  .banner-compat   { top: 160px; }
  .banner-quality  { top: 1178px; }
  .banner-warranty { top: 2195px; }
  .banner-eco      { top: 3213px; }

  .line { position: absolute; line-height: 1; transform: translateY(-50%); white-space: nowrap; }
  .fill { position: absolute; inset: 0; }
  .brand-name { position: absolute; line-height: 1; transform: translateY(-50%); font-family: "Poppins", sans-serif; font-weight: 700; letter-spacing: 1px; }

  /* Banner 1 */
  .banner-compat { background: var(--deep-blue); color: var(--white); font-family: "Lato", sans-serif; }
  .compat-backdrop { background: linear-gradient(155deg, #6aa3cf 0%, #3f84bd 22%, #2f6fa9 48%, #3a86c2 72%, #2d6ea8 100%); }
  .banner-compat .centered { left: 0; right: 0; text-align: center; }
  .banner-compat .brand-name { left: 0; right: 0; text-align: center; top: 106px; font-size: 56px; }
  .compat-head { font-weight: 700; font-size: 42px; }
  .compat-sub { font-weight: 300; font-size: 40px; }
  .module-photo {
    position: absolute; left: 153px; top: 469px; width: 599px; height: 256px;
    border-radius: 4px; box-shadow: 0 10px 24px rgba(10,30,60,0.45);
    background: linear-gradient(180deg, #2a2d32 0%, #1b1d21 20%, #cfd6dc 32%, #e9edf0 50%, #1b1d21 64%, #15171a 86%, #d2b46c 89%, #b89448 100%);
  }
  .compat-en-head { font-weight: 700; font-size: 22px; }
  .compat-en-sub { font-weight: 400; font-size: 21px; }

  /* Banner 2 */
  .banner-quality { background: var(--sky-blue); color: var(--white); font-family: "Poppins", sans-serif; }
  .quality-backdrop { background: linear-gradient(120deg, #5cb4e3 0%, #49a6da 45%, #3f9ad2 100%); }
  .banner-quality .brand-name { left: 589px; top: 78px; font-size: 48px; }
  .quality-head { left: 108px; font-weight: 700; font-size: 32px; }
  .quality-en { left: 108px; font-weight: 600; font-size: 16.5px; }
  .bullet { position: absolute; border-radius: 50%; transform: translate(-50%, -50%); }
  .banner-quality .bullet { left: 77px; width: 10px; height: 10px; border: 2px solid rgba(255,255,255,0.85); }

  /* Banner 3 */
  .banner-warranty { background: var(--pale-grey); color: var(--ink); font-family: "Roboto", sans-serif; }
  .banner-warranty .brand-name { right: 72px; top: 130px; font-size: 46px; color: var(--ink); }
  .warranty-head { right: 109px; text-align: right; font-weight: 500; font-size: 31px; }
  .warranty-en { right: 109px; text-align: right; font-weight: 500; font-size: 16px; }
  .banner-warranty .bullet { left: 837px; width: 10px; height: 10px; background: var(--band-blue); }
  .banner-warranty .bullet.small { width: 7px; height: 7px; }

  /* Banner 4 */
  .banner-eco { background: var(--white); font-family: "Poppins", sans-serif; }
  .banner-eco .brand-name { left: 70px; top: 82px; font-size: 46px; color: var(--white); }
  .eco-head { left: 118px; font-weight: 700; font-size: 40px; color: var(--white); letter-spacing: 0.5px; }
  .banner-eco .bullet { left: 77px; width: 11px; height: 11px; background: var(--band-blue); }
  .eco-en { top: 857px; font-weight: 700; font-size: 17px; color: var(--ink); }
</style>
</head>
<body>

<section class="banner banner-compat">
  <div class="fill compat-backdrop" role="img" aria-label="Blue-toned photo of a circuit board with a hand in the background"></div>
  <div class="brand-name">KERNOVA</div>
  <div class="line centered compat-head" style="top:223px">ABWÄRTSKOMPATIBEL</div>
  <div class="line centered compat-head" style="top:279px">1600 -&gt; 1333 -&gt; 1066 MHZ (FÜR DDR3)</div>
  <div class="line centered compat-sub" style="top:350px">QUORV-KONFORMITÄT / QUORV-</div>
  <div class="line centered compat-sub" style="top:403px">STANDARD</div>
  <div class="module-photo" role="img" aria-label="Photo of a 2GB DDR2 SO-DIMM laptop memory module with labelled chips and gold contacts"></div>
  <div class="line centered compat-en-head" style="top:785px">DOWNWARDS COMPATIBLE 1600 -&gt; 1333 -&gt; 1066 MHZ (FOR DDR3)</div>
  <div class="line centered compat-en-sub" style="top:835px">QUORV COMPLIANCE / QUORV STANDARD</div>
</section>

<section class="banner banner-quality">
  <div class="fill quality-backdrop" role="img" aria-label="Light blue background with a faint network pattern"></div>
  <svg class="fill" viewBox="0 0 914 914" role="img" aria-label="Photo of a white-gloved hand inserting a memory module into a motherboard">
    <defs>
      <linearGradient id="quality-photo" x1="0.2" y1="0" x2="0.6" y2="1">
        <stop offset="0" stop-color="#2f2d33"/>
        <stop offset="0.3" stop-color="#3b3a40"/>
        <stop offset="0.45" stop-color="#e4e6ea"/>
        <stop offset="0.6" stop-color="#9fb4c8"/>
        <stop offset="0.8" stop-color="#3f6f9e"/>
        <stop offset="1" stop-color="#243a56"/>
      </linearGradient>
    </defs>
    <path d="M52,914 L520,372 L700,185 Q780,110 914,265 L914,914 Z" fill="url(#quality-photo)"/>
    <path d="M40,914 L506,364 L690,172 Q782,92 914,250" fill="none" stroke="#ffffff" stroke-width="10"/>
  </svg>
  <div class="brand-name">KERNOVA</div>
  <span class="bullet" style="top:65px"></span>
  <div class="line quality-head" style="top:65px">Nur Original-Chips</div>
  <div class="line quality-head" style="top:108px">führender Marken</div>
  <span class="bullet" style="top:171px"></span>
  <div class="line quality-head" style="top:171px">Hochwertige</div>
  <div class="line quality-head" style="top:214px">Verarbeitung</div>
  <span class="bullet" style="top:278px"></span>
  <div class="line quality-head" style="top:278px">Hochwertige Materialien</div>
  <span class="bullet" style="top:340px"></span>
  <div class="line quality-head" style="top:340px">Vergoldete Kontakte</div>
  <span class="bullet" style="top:408px;width:8px;height:8px"></span>
  <div class="line quality-en" style="top:408px">Only Original Major</div>
  <div class="line quality-en" style="top:434px">Brand Chips</div>
  <span class="bullet" style="top:484px;width:8px;height:8px"></span>
  <div class="line quality-en" style="top:484px">High Quality Manufacturing</div>
  <span class="bullet" style="top:534px;width:8px;height:8px"></span>
  <div class="line quality-en" style="top:534px">High Quality Materials</div>
  <span class="bullet" style="top:586px;width:8px;height:8px"></span>
  <div class="line quality-en" style="top:586px">Gold Plated Contacts</div>
</section>

<section class="banner banner-warranty">
  <svg class="fill" viewBox="0 0 914 914" role="img" aria-label="Photo of a blue-gloved hand installing a memory module on a motherboard">
    <defs>
      <linearGradient id="warranty-photo" x1="0" y1="0" x2="0.9" y2="1">
        <stop offset="0" stop-color="#3f95dc"/>
        <stop offset="0.25" stop-color="#b9c7d6"/>
        <stop offset="0.45" stop-color="#2c3444"/>
        <stop offset="0.7" stop-color="#3567a8"/>
        <stop offset="0.85" stop-color="#2a3d52"/>
        <stop offset="1" stop-color="#a5643a"/>
      </linearGradient>
    </defs>
    <path d="M0,0 H790 C600,20 470,110 400,260 L0,260 Z" fill="var(--band-blue)"/>
    <path d="M0,118 C240,100 460,220 500,470 C520,640 480,800 420,914 L0,914 Z" fill="url(#warranty-photo)"/>
  </svg>
  <div class="brand-name">KERNOVA</div>
  <div class="line warranty-head" style="top:223px">LEBENSLANGE</div>
  <span class="bullet" style="top:223px"></span>
  <div class="line warranty-head" style="top:270px">GARANTIE</div>
  <div class="line warranty-head" style="top:338px">KEINE FRAGEN</div>
  <span class="bullet" style="top:338px"></span>
  <div class="line warranty-head" style="top:384px">GESTELLT</div>
  <div class="line warranty-head" style="top:454px">KOSTENLOSER</div>
  <span class="bullet" style="top:454px"></span>
  <div class="line warranty-head" style="top:501px">ERSATZ</div>
  <div class="line warranty-head" style="top:546px">INNERHALB VON</div>
  <div class="line warranty-head" style="top:592px">2 WERKTAGEN</div>
  <div class="line warranty-en" style="top:667px">LIFETIME WARRANTY</div>
  <span class="bullet small" style="top:664px"></span>
  <div class="line warranty-en" style="top:729px">NO QUESTIONS ASKED</div>
  <span class="bullet small" style="top:726px"></span>
  <div class="line warranty-en" style="top:792px">COST FREE REPLACEMENT IN</div>
  <span class="bullet small" style="top:789px"></span>
  <div class="line warranty-en" style="top:820px">2 BUSINESS DAYS</div>
</section>

<section class="banner banner-eco">
  <svg class="fill" viewBox="0 0 914 914" role="img" aria-label="Photo of a memory module sliding out of a paper package onto a laptop keyboard">
    <defs>
      <linearGradient id="eco-photo" x1="0.3" y1="0" x2="0.5" y2="1">
        <stop offset="0" stop-color="#e6e7ea"/>
        <stop offset="0.3" stop-color="#c4c7cd"/>
        <stop offset="0.48" stop-color="#2b2b30"/>
        <stop offset="0.65" stop-color="#3a3a40"/>
        <stop offset="1" stop-color="#57575e"/>
      </linearGradient>
    </defs>
    <rect x="0" y="0" width="914" height="830" fill="var(--charcoal)"/>
    <path d="M430,0 H914 V820 L560,820 C580,600 600,420 640,260 C680,130 740,40 770,0 Z" fill="url(#eco-photo)"/>
    <path d="M430,0 H780 C730,60 700,120 675,170 C600,150 540,130 460,135 Z" fill="var(--white)"/>
    <path d="M0,0 H430 C420,110 380,155 300,165 L0,230 Z" fill="var(--band-blue)"/>
    <path d="M0,825 C220,790 420,780 600,775 C760,770 860,750 914,725 V914 H0 Z" fill="var(--white)"/>
  </svg>
  <div class="brand-name">KERNOVA</div>
  <span class="bullet" style="top:309px"></span>
  <div class="line eco-head" style="top:311px">95 % WENIGER</div>
  <div class="line eco-head" style="top:366px">PLASTIK</div>
  <span class="bullet" style="top:462px"></span>
  <div class="line eco-head" style="top:464px">GUT FÜR DEN</div>
  <div class="line eco-head" style="top:519px">PLANETEN</div>
  <span class="bullet" style="top:615px"></span>
  <div class="line eco-head" style="top:617px">INNOVATIVE</div>
  <div class="line eco-head" style="top:672px">VERPACKUNG</div>
  <div class="line eco-en" style="left:106px">95% LESS PLASTIC</div>
  <div class="line eco-en" style="left:290px">/</div>
  <div class="line eco-en" style="left:324px">GOOD FOR THE PLANET</div>
  <div class="line eco-en" style="left:553px">/</div>
  <div class="line eco-en" style="left:586px">INNOVATIVE PACKAGING</div>
</section>

</body>
</html>
```